Window Decal for Speech, Feeding, Occupational, Physical, and Behavior Therapy office for children

I need a high resolution, vertical design, preferably via Adobe Illustrator (real size design) that can be applied to office store front windows, in the form of window decals. The business is called Bright Steps Therapy and we provide Speech, Feeding, Occupational, Physical and Behavior Therapy for children; therefore, the design must be relay a kid-friendly image, while highlighting conditions we treat/service. We are looking to apply signage to (4) glass windows and (1) glass entry door. I have uploaded (3) attachments - a draft design (with window measurements), our company logo and an image of the store front.

Target Market(s)

Parents

Industry/Entity Type

Healthcare

Colors

Designer to choose colors to be used in the design.

Requirements
Must have
• Imagery must be high resolution
• The logo is trademarked, so it must stay the same.
• The (3) window design of the faces blowing bubbles, with the depicted wording is necessary; however, the imagery and layout can both be improved upon, yet I still need a resemblance to what is provided. Additionally, I've added (2) new facial images from the interior walls of our clinic. My preference is to have the faces for the exterior windows mirror these images as closely as possible in terms of skin tone (darkness), definition and realism.
• Also, please provide bleed room along the edges in your design.

```html
<!DOCTYPE html>
<html lang="en">
<head>
<meta charset="utf-8">
<title>Bright Steps Therapy – Window Decals</title>
<link href="https://fonts.googleapis.com/css2?family=Oswald:wght@500;600&family=Source+Sans+3:wght@400;600;700&display=swap" rel="stylesheet">
<style>
  :root{
    --page:#ffffff;
    --frame:#2b2b2b;
    --ink:#2a2a2a;
    --red:#c8102e;
    --cyan:#00a9e0;
    --purple:#7a2a8c;
    --navy:#263a8a;
    --brown:#5a3a1c;
    --orange:#f08a1c;
    --magenta:#d61a7a;
    --teal:#10968c;
    --coral:#ef4b23;
    --band-green:#21b36b;
    --band-blue:#1e7ec8;
    --band-purple:#6a2d91;
  }
  html,body{margin:0;padding:0;width:1200px;height:849px;overflow:hidden;background:var(--page)}
  .decal-sheet{display:block;width:1200px;height:849px}
  .body-text{font-family:"Source Sans 3",sans-serif;fill:var(--ink)}
  .headline{font-family:"Oswald",sans-serif;font-weight:600;text-anchor:middle;letter-spacing:.2px}
  .center{text-anchor:middle}
  .panel-frame{fill:url(#silver);stroke:var(--frame);stroke-width:1.6}
</style>
</head>
<body>
<svg class="decal-sheet" viewBox="0 0 1200 849" xmlns="http://www.w3.org/2000/svg">
  <defs>
    <linearGradient id="silver" x1="0" x2="1" y1="0" y2="0">
      <stop offset="0" stop-color="#b9b9bb"/>
      <stop offset=".45" stop-color="#f6f6f7"/>
      <stop offset=".6" stop-color="#ffffff"/>
      <stop offset="1" stop-color="#a9a9ab"/>
    </linearGradient>
    <radialGradient id="bubble-red" cx=".4" cy=".35" r=".65">
      <stop offset="0" stop-color="#fff" stop-opacity=".7"/>
      <stop offset=".6" stop-color="#f6a3a3" stop-opacity=".6"/>
      <stop offset="1" stop-color="#e0242c"/>
    </radialGradient>
    <radialGradient id="bubble-blue" cx=".4" cy=".35" r=".65">
      <stop offset="0" stop-color="#fff" stop-opacity=".7"/>
      <stop offset=".6" stop-color="#a9b3e0" stop-opacity=".6"/>
      <stop offset="1" stop-color="#2c3a92"/>
    </radialGradient>
    <radialGradient id="bubble-green" cx=".4" cy=".35" r=".65">
      <stop offset="0" stop-color="#fff" stop-opacity=".7"/>
      <stop offset=".6" stop-color="#b8e3c4" stop-opacity=".6"/>
      <stop offset="1" stop-color="#1f9a4a"/>
    </radialGradient>
    <radialGradient id="bubble-big" cx=".45" cy=".4" r=".6">
      <stop offset="0" stop-color="#eaf7ee" stop-opacity=".8"/>
      <stop offset=".7" stop-color="#9fd7ae" stop-opacity=".85"/>
      <stop offset="1" stop-color="#12853a"/>
    </radialGradient>
    <linearGradient id="girl-tones" x1="0" x2="1">
      <stop offset="0" stop-color="#3b2518"/>
      <stop offset=".35" stop-color="#5a3a24"/>
      <stop offset=".6" stop-color="#b87a4f"/>
      <stop offset="1" stop-color="#c98d5e"/>
    </linearGradient>
    <linearGradient id="boy-tones" x1="0" x2="1">
      <stop offset="0" stop-color="#d99a68"/>
      <stop offset=".7" stop-color="#c07a48"/>
      <stop offset="1" stop-color="#3a2416"/>
    </linearGradient>
    <symbol id="bubble-shine" viewBox="0 0 10 10"><circle cx="5" cy="5" r="5" fill="#fff"/></symbol>
  </defs>

  <!-- Entry door panel -->
  <g class="door-panel">
    <rect class="panel-frame" x="78" y="183" width="130" height="408"/>
    <line x1="78" y1="304" x2="208" y2="304" stroke="var(--frame)" stroke-width="1.4"/>
    <circle cx="98" cy="372" r="6" fill="var(--band-blue)"/>
    <text class="body-text" x="108" y="370" font-size="15" font-weight="600">Bright Steps</text>
    <text class="body-text" x="108" y="387" font-size="15" font-weight="600">Therapy</text>
    <text class="body-text center" x="143" y="420" font-size="7" font-weight="700">“...where serving you is therapeutic!”</text>
    <text class="body-text center" x="143" y="437" font-size="7" font-weight="700">Hours: 9 a.m. – 8 p.m.</text>
    <text class="body-text center" x="143" y="446" font-size="7" font-weight="700">Phone: 555-014-2870</text>
    <text class="body-text center" x="143" y="464" font-size="8" font-weight="700">Follow @brightstepskids</text>
  </g>

  <!-- Single window panel -->
  <g class="info-panel">
    <rect class="panel-frame" x="231" y="183" width="162" height="408"/>
    <circle cx="270" cy="220" r="22" fill="url(#bubble-red)"/>
    <circle cx="354" cy="206" r="21" fill="url(#bubble-blue)"/>
    <text class="body-text center" x="312" y="273" font-size="9" font-weight="600">“Getting Our Kids Back on Track”</text>
    <circle cx="314" cy="299" r="17" fill="url(#bubble-green)"/>
    <circle cx="351" cy="334" r="22" fill="url(#bubble-red)"/>
    <circle cx="258" cy="346" r="6" fill="var(--band-blue)"/>
    <text class="body-text" x="268" y="350" font-size="18" font-weight="600">Bright Steps</text>
    <text class="body-text" x="268" y="372" font-size="18" font-weight="600">Therapy</text>
    <circle cx="287" cy="400" r="20" fill="url(#bubble-blue)"/>
    <circle cx="374" cy="398" r="14" fill="url(#bubble-blue)"/>
    <rect x="231" y="410" width="45" height="12" fill="var(--band-green)"/>
    <rect x="276" y="410" width="44" height="12" fill="var(--band-blue)"/>
    <rect x="320" y="410" width="73" height="12" fill="var(--band-purple)"/>
    <g class="body-text" font-size="9" font-weight="700" fill="#fff" style="fill:#fff">
      <text x="253" y="419" text-anchor="middle" fill="#fff">Speech</text>
      <text x="298" y="419" text-anchor="middle" fill="#fff">Feeding</text>
      <text x="356" y="419" text-anchor="middle" fill="#fff">Occupational</text>
    </g>
    <circle cx="312" cy="448" r="14" fill="url(#bubble-green)" opacity=".7"/>
    <text class="body-text center" x="310" y="445" font-size="10" font-weight="600">Applied Behavior Analysis</text>
    <text class="body-text center" x="310" y="458" font-size="10" font-weight="600">Physical Therapy</text>
    <text class="body-text center" x="312" y="511" font-size="13" font-weight="600">“You Are Not Alone.”</text>
    <circle cx="327" cy="530" r="6" fill="url(#bubble-blue)"/>
    <circle cx="306" cy="548" r="9" fill="url(#bubble-red)"/>
    <circle cx="355" cy="546" r="6" fill="url(#bubble-green)"/>
    <circle cx="342" cy="562" r="8" fill="url(#bubble-blue)"/>
    <circle cx="258" cy="565" r="8" fill="url(#bubble-blue)"/>
    <circle cx="299" cy="567" r="7" fill="url(#bubble-green)"/>
  </g>

  <!-- Triple window panel -->
  <g class="bubble-mural">
    <rect class="panel-frame" x="417" y="183" width="691" height="408"/>
    <rect role="img" aria-label="Illustration of a girl in profile with long dark hair, eyes closed, blowing bubbles through a wand" x="418" y="184" width="164" height="406" fill="url(#girl-tones)"/>
    <rect role="img" aria-label="Illustration of a boy in profile with short dark hair, eyes closed, blowing bubbles through a wand" x="988" y="184" width="118" height="406" fill="url(#boy-tones)"/>
    <line x1="647" y1="183" x2="647" y2="591" stroke="var(--frame)" stroke-width="1.4"/>
    <line x1="878" y1="183" x2="878" y2="591" stroke="var(--frame)" stroke-width="1.4"/>

    <circle cx="762" cy="296" r="104" fill="url(#bubble-big)"/>
    <circle cx="574" cy="210" r="20" fill="url(#bubble-green)"/>
    <circle cx="598" cy="269" r="27" fill="url(#bubble-blue)"/>
    <circle cx="608" cy="340" r="30" fill="url(#bubble-red)"/>
    <circle cx="828" cy="240" r="21" fill="url(#bubble-blue)"/>
    <circle cx="808" cy="392" r="22" fill="url(#bubble-green)"/>
    <circle cx="812" cy="457" r="30" fill="url(#bubble-red)"/>
    <circle cx="796" cy="505" r="30" fill="url(#bubble-red)"/>
    <circle cx="706" cy="490" r="27" fill="url(#bubble-blue)"/>
    <circle cx="807" cy="547" r="18" fill="url(#bubble-blue)"/>
    <circle cx="702" cy="559" r="19" fill="url(#bubble-green)"/>
    <circle cx="958" cy="241" r="36" fill="url(#bubble-green)"/>
    <circle cx="917" cy="315" r="27" fill="url(#bubble-blue)"/>
    <circle cx="994" cy="372" r="38" fill="url(#bubble-red)"/>
    <circle cx="942" cy="454" r="22" fill="url(#bubble-green)"/>

    <text class="headline" x="612" y="238" font-size="24" fill="var(--red)">PICKY</text>
    <text class="headline" x="612" y="271" font-size="24" fill="var(--red)">EATER</text>
    <text class="headline" x="610" y="336" font-size="24" fill="var(--cyan)">AUTISM</text>
    <text class="headline" x="760" y="236" font-size="17" fill="var(--purple)">IS YOUR CHILD</text>
    <text class="headline" x="762" y="261" font-size="17" fill="var(--purple)">ON TRACK?</text>
    <text class="headline" x="768" y="292" font-size="17" fill="var(--navy)">EARLY INTERVENTION MATTERS</text>
    <text class="headline" x="762" y="327" font-size="11" fill="var(--brown)">SPEECH | OCCUPATIONAL | PHYSICAL THERAPY</text>
    <text class="headline" x="694" y="394" font-size="24" fill="var(--orange)">VOICE</text>
    <text class="headline" x="694" y="427" font-size="24" fill="var(--orange)">DISORDER</text>
    <text class="headline" x="815" y="435" font-size="24" fill="var(--magenta)">BALANCE</text>
    <text class="headline" x="812" y="467" font-size="24" fill="var(--magenta)">&amp;</text>
    <text class="headline" x="815" y="500" font-size="24" fill="var(--magenta)">COORDINATION</text>
    <text class="headline" x="742" y="534" font-size="24" fill="var(--brown)">ARTICULATION</text>
    <text class="headline" x="945" y="250" font-size="24" fill="var(--purple)">SOCIAL</text>
    <text class="headline" x="948" y="283" font-size="24" fill="var(--purple)">SKILLS</text>
    <text class="headline" x="962" y="338" font-size="24" fill="var(--teal)">TOE</text>
    <text class="headline" x="966" y="371" font-size="24" fill="var(--teal)">WALKING</text>
    <text class="headline" x="926" y="416" font-size="24" fill="var(--coral)">SPEECH</text>
    <text class="headline" x="926" y="448" font-size="24" fill="var(--coral)">DELAY</text>
    <text class="headline" x="932" y="523" font-size="24" fill="var(--navy)">STUTTERING</text>
  </g>
</svg>
</body>
</html>
```